Media and Film Company Needs a New Website

We produce highly stylized commercials and film pieces for our clients. We also produce live events, both corporate and theatrical. Looking for a site that can show off our client videos - have a polished way to show off our team, and be able to create pages to highlight our clients and give a full overview of our project/process with them. We design simple website for some of our clients - so we are very wordpress familiar, and would like something that doesn't feel like a template.

Target Market(s)

content creators, creative directors, production teams, marketing agencies

Industry/Entity Type

Film Production

Number of Pages Required

4 page

Font styles to use
Sans Serif

Requirements
Must have
• slick looking video embed (from YT or Vimeo)
• project pages - client snapshot (what we did for them, how we did it)
• nice landing page, have our company video reel on the page
• testimonials
• contact page
• ability to have photos as a background if we want
Nice to have
• polished clean look - look to our logo colors and linear elements
• we produce very stylized videos for our clients and our website should reflect that
Should not have
• template look or feel to it- please bring your flare to the project!
• take a look at our current site - zantorvo.com we need a better way to highlight our work and our clients

```html
<!DOCTYPE html>
<html lang="en">
<head>
<meta charset="utf-8">
<title>Zantorvo Media &amp; Entertainment</title>
<link rel="stylesheet" href="https://fonts.googleapis.com/css2?family=Poppins:wght@300;400;500;600&display=swap">
<style>
:root{
  --ink:#1e1e1e;
  --dark:#222325;
  --hero-a:#3a3f47;
  --hero-b:#15171b;
  --muted:#8a8a8a;
  --line:#e2e2e2;
  --soft:#f3f3f3;
  --accent:#e8c23a;
  --accent-bg:#3b3720;
  --white:#ffffff;
  --link:#6f9fd8;
}
*{box-sizing:border-box;margin:0;padding:0}
html,body{width:1200px;height:2316px;overflow:hidden}
body{font-family:"Poppins",sans-serif;color:var(--ink);background:var(--white);position:relative}
.hero{position:absolute;top:0;left:0;width:1200px;height:500px;overflow:hidden}
.hero-media{position:absolute;inset:0;background:linear-gradient(180deg,var(--hero-a) 0%,#2a2e35 55%,var(--hero-b) 100%)}
.nav{position:absolute;top:22px;left:88px;right:86px;height:44px;display:flex;align-items:center}
.brand{display:flex;align-items:center;gap:8px;color:var(--white);font-weight:600;font-size:18px;letter-spacing:1px}
.brand-mark{width:14px;height:14px;border-radius:50%;background:var(--white)}
.nav-links{display:flex;gap:34px;margin-left:auto;margin-right:auto;list-style:none}
.nav-links li{font-size:11px;letter-spacing:1px;color:#d7d7d7}
.nav-links li.active{color:var(--accent)}
.btn-outline{border:1.5px solid var(--white);color:var(--white);border-radius:22px;padding:9px 18px;font-size:11px;letter-spacing:1px}
.hero-copy{position:absolute;left:88px;top:232px;color:var(--white)}
.hero-copy h1{font-size:38px;font-weight:500;line-height:1.2}
.hero-copy p{font-size:15px;margin-top:6px;font-weight:400;line-height:1.5}
.play-dot{position:absolute;left:88px;top:332px;width:26px;height:26px;border-radius:50%;background:rgba(255,255,255,.12);display:flex;align-items:center;justify-content:center}
.section-title{font-size:24px;font-weight:600}
.videos{position:absolute;top:500px;left:0;width:1200px;height:520px;overflow:hidden}
.videos .section-title{position:absolute;left:88px;top:70px}
.arrows{position:absolute;right:90px;top:68px;display:flex;gap:10px}
.arrows span{width:34px;height:34px;border-radius:50%;border:1px solid var(--line);display:flex;align-items:center;justify-content:center}
.video-row{position:absolute;top:152px;left:88px;display:flex;gap:12px}
.card{position:relative;width:248px;height:300px;overflow:hidden;flex:none}
.card .media{position:absolute;inset:0}
.card .caption{position:absolute;left:20px;bottom:22px;color:var(--white);font-size:15px;font-weight:500;white-space:nowrap}
.card .play{position:absolute;left:20px;top:180px}
.photos{position:absolute;top:1020px;left:0;width:1200px;height:540px;background:var(--soft)}
.centered{text-align:center}
.photos .section-title{position:absolute;top:56px;width:100%}
.photo-row{position:absolute;top:132px;left:88px;display:flex;gap:12px}
.photo{position:relative;width:334px;height:296px;overflow:hidden}
.photo .media{position:absolute;inset:0}
.photo .tag{position:absolute;left:20px;bottom:20px;display:flex;align-items:center;gap:12px;color:var(--white);font-size:14px;font-weight:500;white-space:nowrap}
.photo .tag i{width:34px;height:34px;border-radius:4px;background:rgba(255,255,255,.18);display:block;flex:none}
.pill{position:absolute;left:50%;transform:translateX(-50%);border:1px solid var(--line);border-radius:16px;padding:7px 20px;font-size:9px;letter-spacing:1px;color:var(--link);background:var(--white);white-space:nowrap}
.team{position:absolute;top:1560px;left:0;width:1200px;height:520px}
.team .section-title{position:absolute;top:56px;width:100%}
.team-row{position:absolute;top:120px;left:88px;display:flex;gap:12px}
.member{position:relative;width:248px;height:296px;overflow:hidden}
.member .media{position:absolute;inset:0}
.member .info{position:absolute;left:20px;bottom:20px;color:var(--white)}
.member .info b{display:block;font-size:16px;font-weight:600}
.member .info span{font-size:10px;color:#d0d0d0}
.footer{position:absolute;top:2080px;left:0;width:1200px;height:236px;background:var(--dark);color:var(--white)}
.footer h2{position:absolute;top:66px;width:100%;text-align:center;font-size:17px;font-weight:500}
.email-btn{position:absolute;top:114px;left:50%;transform:translateX(-50%);background:var(--accent-bg);color:var(--accent);border-radius:18px;padding:9px 22px;font-size:11px;white-space:nowrap}
.legal{position:absolute;bottom:14px;left:88px;right:90px;display:flex;justify-content:space-between;font-size:10px;color:#cfcfcf;border-top:1px solid #34363a;padding-top:12px}
.legal nav{display:flex;gap:40px}
</style>
</head>
<body>
<header class="hero">
  <div class="hero-media" role="img" aria-label="Dark photo of a person silhouetted against an airport window with a jet outside"></div>
  <div class="nav">
    <div class="brand"><span class="brand-mark"></span>ZANTORVO</div>
    <ul class="nav-links">
      <li class="active">HOME</li><li>PORTFOLIO</li><li>ABOUT ZTV</li><li>TESTIMONIALS</li><li>PRESS</li>
    </ul>
    <div class="btn-outline">CONTACT US</div>
  </div>
  <div class="hero-copy">
    <h1>Watch our 2015 Demo Reel</h1>
    <p>We provide full-service campaigns in film and media production.</p>
  </div>
  <div class="play-dot"><svg width="8" height="10" viewBox="0 0 8 10"><path d="M0 0L8 5L0 10Z" fill="#5fa0e0"/></svg></div>
</header>

<section class="videos">
  <h2 class="section-title">Latest Videos</h2>
  <div class="arrows">
    <span><svg width="8" height="10" viewBox="0 0 8 10"><path d="M6 1L2 5L6 9" stroke="#999" fill="none"/></svg></span>
    <span><svg width="8" height="10" viewBox="0 0 8 10"><path d="M2 1L6 5L2 9" stroke="#999" fill="none"/></svg></span>
  </div>
  <div class="video-row">
    <div class="card"><div class="media" role="img" aria-label="Concert crowd under warm orange stage light" style="background:linear-gradient(160deg,#c7702d,#5a2a14 60%,#1c100b)"></div><svg class="play" width="14" height="16" viewBox="0 0 14 16"><path d="M0 0L14 8L0 16Z" fill="#fff"/></svg><div class="caption">Harbor Stage</div></div>
    <div class="card"><div class="media" role="img" aria-label="Children at an outdoor anniversary celebration" style="background:linear-gradient(160deg,#4a5a6a,#8a4a3a 55%,#2a2020)"></div><svg class="play" width="14" height="16" viewBox="0 0 14 16"><path d="M0 0L14 8L0 16Z" fill="#fff"/></svg><div class="caption">KLT 20TH ANNIVE...</div></div>
    <div class="card"><div class="media" role="img" aria-label="Suburban house at dusk under a blue sky" style="background:linear-gradient(180deg,#6f8fc8,#9aa8c8 50%,#5a4a48)"></div><svg class="play" width="14" height="16" viewBox="0 0 14 16"><path d="M0 0L14 8L0 16Z" fill="#fff"/></svg><div class="caption">Hollins Deli and S...</div></div>
    <div class="card"><div class="media" role="img" aria-label="Dim studio interior with warm haze" style="background:linear-gradient(160deg,#7a5a4a,#3a2a26 60%,#1a1515)"></div><svg class="play" width="14" height="16" viewBox="0 0 14 16"><path d="M0 0L14 8L0 16Z" fill="#fff"/></svg><div class="caption">Introducing Dr. Vel...</div></div>
    <div class="card"><div class="media" role="img" aria-label="Bright event venue" style="background:linear-gradient(160deg,#d8d0c8,#a89888)"></div></div>
  </div>
</section>

<section class="photos">
  <h2 class="section-title centered">Featured Photos</h2>
  <div class="photo-row">
    <div class="photo"><div class="media" role="img" aria-label="Speaker with a microphone on a dark stage" style="background:linear-gradient(150deg,#3a3a3a,#151515 70%)"></div><div class="tag"><i></i>Riverlight Docs Film Festival</div></div>
    <div class="photo"><div class="media" role="img" aria-label="Speaker at a podium before a blue backdrop" style="background:linear-gradient(160deg,#2a5aa0,#4a6a9a 50%,#2a2a30)"></div><div class="tag"><i></i>Capitol hall student film fes...</div></div>
    <div class="photo"><div class="media" role="img" aria-label="Group of students gathered at a master class" style="background:linear-gradient(160deg,#b8aaa0,#7a6058 55%,#3a2a28)"></div><div class="tag"><i></i>Master Class with Marla Pen...</div></div>
  </div>
  <div class="pill" style="top:476px">SEE OUR PORTFOLIO</div>
</section>

<section class="team">
  <h2 class="section-title centered">Meet the team</h2>
  <div class="team-row">
    <div class="member"><div class="media" role="img" aria-label="Black and white portrait of a team member" style="background:linear-gradient(160deg,#6a6a6a,#1c1c1c)"></div><div class="info"><b>Member name</b><span>Member's position in company</span></div></div>
    <div class="member"><div class="media" role="img" aria-label="Portrait of a team member in a grey jacket" style="background:linear-gradient(160deg,#c8ccd0,#6a6e74 60%,#2a2c30)"></div><div class="info"><b>Member name</b><span>Member's position in company</span></div></div>
    <div class="member"><div class="media" role="img" aria-label="Portrait of a team member in a denim jacket" style="background:linear-gradient(160deg,#c8c0b8,#7a6a5c 55%,#2a2420)"></div><div class="info"><b>Member name</b><span>Member's position in company</span></div></div>
    <div class="member"><div class="media" role="img" aria-label="Portrait of a team member outdoors in warm light" style="background:linear-gradient(160deg,#8a5a3a,#c08a5a 50%,#2a1c14)"></div><div class="info"><b>Member name</b><span>Member's position in company</span></div></div>
  </div>
  <div class="pill" style="top:460px">MORE MEMBERS</div>
</section>

<footer class="footer">
  <h2>Ready to get to work? Contact us today.</h2>
  <div class="email-btn">Email us at hello@zantorvo.com</div>
  <div class="legal">
    <span>©2015 Zantorvo Media &amp; Entertainment</span>
    <nav><span>Terms &amp; Conditions</span><span>Privacy Policy</span></nav>
  </div>
</footer>
</body>
</html>
```